Vereins Website
Super tolles Design & sehr freundliche Kommunikation. Alle Änderungswünsche wurden sofort umgesetzt. Hat super Spass gemacht, danke! :)
Zielgruppe
Webiste für den Verein 'Fellacker Tiefmatt' (details siehe Anhang).
Ziel der Website:
- Sponsoren finden
- Vereinsmitglieder finden & Interessen bündeln.
Aufgabenstellung
Die Webiste sollt aufgeräumt, übersichtlich und freundlich wirken.

```html
<!DOCTYPE html>
<html lang="de">
<head>
<meta charset="utf-8">
<title>Verein Fellacker Tiefmatt</title>
<link rel="stylesheet" href="https://fonts.googleapis.com/css2?family=Arimo:wght@400;700&display=swap">
<style>
:root{
  --green:#72aa6a;
  --green-text:#6aa662;
  --green-field:#8fc888;
  --green-deep:#6aa662;
  --dark:#2d2d2d;
  --ink:#1e1e1e;
  --white:#ffffff;
  --grey-light:#e5e5e5;
  --grey-box:#e0e0e0;
  --grey-box-dark:#c4c4c4;
  --grey-btn:#dcdcdc;
  --grey-footer:#7d7d7d;
}
*{margin:0;padding:0;box-sizing:border-box}
html,body{width:1200px;height:3456px;overflow:hidden;background:var(--white)}
body{position:relative;font-family:"Arimo",Arial,sans-serif;color:var(--ink)}
.abs{position:absolute}
.center{left:0;width:1200px;text-align:center}

.site-header{top:0;left:0;width:1200px;height:160px;background:var(--green)}
.site-header .kicker{top:64px;font-size:19px;line-height:22px;letter-spacing:7px;color:var(--ink)}
.site-header .name{top:90px;font-size:40px;line-height:46px;font-weight:700;letter-spacing:2px;color:var(--white);text-transform:uppercase}

.hero{top:160px;left:0;width:1200px;height:620px;background:linear-gradient(180deg,#d9dcd8 0%,#5d6b4d 22%,#b98a58 45%,#a8652a 65%,#c9a37a 100%)}

.intro-title{top:893px;font-size:34px;font-weight:700;letter-spacing:2px;line-height:40px;color:var(--green-text)}
.intro-text{top:989px;font-size:14px;letter-spacing:3.2px;line-height:25px;color:var(--ink)}
.intro-text b{font-weight:700}

.form-title{top:1311px;font-size:24px;line-height:28px;font-weight:700;letter-spacing:2px}
.label{font-size:14px;line-height:16px;letter-spacing:3.4px}
.field{background:var(--green-field)}
.btn{font-size:11px;letter-spacing:3px;text-align:center;line-height:38px}
.btn-grey{background:var(--grey-btn);box-shadow:0 2px 3px rgba(0,0,0,.25);color:var(--ink)}
.form-note{top:1820px;font-size:15px;letter-spacing:.5px;line-height:19px}

.help-title{top:1976px;font-size:42px;line-height:46px;font-weight:700;letter-spacing:3px;color:var(--green-text)}
.help-sub{top:2025px;font-size:26px;line-height:30px;letter-spacing:5px}

.bar-dark{background:var(--dark);color:var(--white);font-weight:700;letter-spacing:1.5px}
.logo-slot{background:var(--grey-box)}
.logo-slot.featured{background:var(--grey-box-dark);color:var(--white);font-size:19px;letter-spacing:1px;line-height:25px;display:flex;align-items:center;justify-content:center;text-align:center}
.sponsor-photo{top:2090px;left:702px;width:498px;height:469px;background:linear-gradient(180deg,#b9a46e 0%,#9fae57 50%,#c4d565 100%)}

.account{top:2559px;left:0;width:497px;height:470px;background:var(--green-deep);color:var(--white);text-align:center}
.account h3{position:absolute;top:134px;left:0;width:497px;font-size:30px;line-height:34px;letter-spacing:2px}
.account p{position:absolute;left:0;width:497px;font-size:19px;line-height:22px;letter-spacing:1px}

.pay-name{font-size:28px;font-weight:700;color:var(--ink);display:flex;align-items:center;gap:12px;justify-content:center}
.pay-name i{display:inline-block;width:16px;height:16px;background:var(--ink)}
.slip{border:3px solid #7a7a7a;font-size:16px;letter-spacing:1.5px;text-align:center;line-height:32px}

.contact{top:3029px;left:0;width:1200px;height:370px;background:var(--grey-light)}
.contact-title{top:3087px;font-size:21px;line-height:24px;font-weight:700;letter-spacing:1.5px}
.input-white{background:var(--white);font-size:14px;line-height:16px;letter-spacing:3px;padding:14px 12px}
.btn-green{background:var(--green);color:var(--white);box-shadow:0 2px 3px rgba(0,0,0,.25)}
.site-footer{top:3399px;left:0;width:1200px;height:57px;background:var(--grey-footer)}
</style>
</head>
<body>

<header class="abs site-header">
  <div class="abs center kicker">VEREIN</div>
  <div class="abs center name">Fellacker Tiefmatt</div>
</header>

<div class="abs hero" role="img" aria-label="Foto: Hund wälzt sich auf dem Rücken im trockenen Gras"></div>

<h1 class="abs center intro-title">EIN BEGEGNUNGSORT FÜR DIE GANZE REGION,<br>VON DEM ALLE PROFITIEREN.</h1>
<p class="abs center intro-text">NACH DEM VORBILD VON <b>OSTWIL</b> MÖCHTEN WIR IN TIEFMATT EINE<br>EINGEZÄUNTE HUNDESPIELWIESE AUF DIE BEINE STELLEN UND DAMIT<br>DAS WOHLERGEHEN DER HUNDE FÖRDERN.<br>AUF DER EINGEZÄUNTEN WIESE KÖNNEN DIE HUNDE OHNE LEINENZWANG<br>SPIELEN, SICH AUSTOBEN UND SOZIALISIEREN.<br>GLEICHZEITIG SCHAFFT DIES EINEN RAUM, IN DEM SICH DIE HUNDEHAL-<br>TER TREFFEN UND AUSTAUSCHEN KÖNNEN.</p>

<h2 class="abs center form-title">PROJEKT UNTERSTÜTZEN UND VEREINSMITGLIED* WERDEN:</h2>
<div class="abs label" style="top:1376px;left:246px">VORNAME</div>
<div class="abs label" style="top:1376px;left:623px">NACHNAME</div>
<div class="abs field" style="top:1404px;left:235px;width:355px;height:44px"></div>
<div class="abs field" style="top:1404px;left:612px;width:356px;height:44px"></div>
<div class="abs label" style="top:1469px;left:246px">STRASSE | HAUSNUMMER</div>
<div class="abs field" style="top:1496px;left:235px;width:733px;height:45px"></div>
<div class="abs label" style="top:1562px;left:246px">PLZ | ORT</div>
<div class="abs field" style="top:1589px;left:235px;width:733px;height:44px"></div>
<div class="abs label" style="top:1654px;left:246px">E-MAIL-ADRESSE</div>
<div class="abs field" style="top:1682px;left:235px;width:733px;height:44px"></div>
<div class="abs btn btn-grey" style="top:1751px;left:476px;width:210px;height:38px">ABSENDEN</div>
<p class="abs center form-note">EINE VEREINSMITGLIEDSCHAFT IST DERZEIT NOCH KOSTENLOS.<br>SIE UNTERSTÜTZEN DEN VEREIN DAMIT IDEELL.</p>

<h2 class="abs center help-title">HELFEN SIE UNS</h2>
<p class="abs center help-sub">DIESES PROJEKT ZU VERWIRKLICHEN</p>

<section>
  <div class="abs bar-dark" style="top:2090px;left:0;width:702px;height:92px;font-size:32px;line-height:92px;text-align:center">FÜR SPONSOREN</div>
  <div class="abs logo-slot" style="top:2228px;left:64px;width:133px;height:131px"></div>
  <div class="abs logo-slot" style="top:2228px;left:213px;width:132px;height:131px"></div>
  <div class="abs logo-slot featured" style="top:2228px;left:362px;width:281px;height:131px">HIER KÖNNTE<br>IHR LOGO STEHEN</div>
  <div class="abs logo-slot" style="top:2374px;left:64px;width:281px;height:132px"></div>
  <div class="abs logo-slot" style="top:2374px;left:362px;width:132px;height:132px"></div>
  <div class="abs logo-slot" style="top:2374px;left:511px;width:132px;height:132px"></div>
  <div class="abs sponsor-photo" role="img" aria-label="Foto: junger Spaniel rennt mit einem Ball über die Wiese"></div>
</section>

<section>
  <div class="abs account">
    <h3>SPENDENKONTO:</h3>
    <p style="top:182px">FELLACKER TIEFMATT</p>
    <p style="top:219px">IBAN: 41 27350 81946 05213 7</p>
    <p style="top:257px">BIC: 2918406</p>
  </div>
  <div class="abs bar-dark" style="top:2559px;left:497px;width:703px;height:94px;font-size:25px;line-height:94px;padding-left:40px">FÜR PRIVATE SPENDEN</div>
  <div class="abs pay-name" style="top:2716px;left:580px;width:244px;height:60px"><i></i>Zahlfix</div>
  <div class="abs slip" style="top:2731px;left:862px;width:238px;height:38px">EINZAHLUNGSSCHEIN</div>
  <div class="abs pay-name" style="top:2824px;left:640px;width:160px;height:103px">Tippay</div>
  <div class="abs pay-name" style="top:2824px;left:816px;width:284px;height:103px"><i></i>Postkasse</div>
</section>

<section class="abs contact"></section>
<h2 class="abs center contact-title">WIR FREUEN UNS AUF IHRE ANREGUNGEN &amp; IDEEN:</h2>
<div class="abs input-white" style="top:3134px;left:231px;width:355px;height:44px">NAME</div>
<div class="abs input-white" style="top:3134px;left:609px;width:356px;height:44px">E-MAIL-ADRESSE</div>
<div class="abs input-white" style="top:3199px;left:231px;width:734px;height:90px;padding-top:12px">IHRE NACHRICHT</div>
<div class="abs btn btn-green" style="top:3304px;left:472px;width:210px;height:38px">ABSENDEN</div>

<footer class="abs site-footer"></footer>
</body>
</html>
```